Coupons App Design Project

We have a simple coupons app with few screens and actions:
1. Very simple login screen (with chatterloop and findwell+)
2. Very simple business search page
3. Very simple business search results(each result contains logo icon, business name and delete icon)
4. business list (every row contains logo icon, business name and delete icon)
5. coupons list (each item contains image, title, subtitle, description, expiration time, status graphics (valid, expired, redeemed), delete icon
6. coupon view (image, title, subtitle, description, barcode etc.)
7. custom confirmation dialog(title, buttons, background, text)
8. "scan to subscribe" page (merchant name, merchant number, background image, text, barcode to scan etc.)
9. simple menu
10. splash screen

all graphics should be vector graphics so we can use it to different resolutions including for printing
Updates

Hi all, We've increased the project's budget by 25%. Thanks

Hi all,

We've decided to change the project from refundable to committed payment.
FYI

Hi All,

Thank you for your time and efforts, we really appreciate it.However we've eliminated most of the offered designs we've received becausethey didn't fit our desired look and feel.

Please download our look and feel file from our uploaded files -we've put there some examples of other apps that we like.

Thanks

Target Market(s)

shoppers all over the world

Industry/Entity Type

Business

Requirements
Must have
• Please take a look at the attached file "look & feel.jpg" for some nice screen shots taken from apps that we like

Should not have
• *****************************************************************************************
The attached files are only for demonstration purpose and needs descriptions so please don't send us design based on these screenshots.
*****************************************************************************************

```html
<!DOCTYPE html>
<html lang="en">
<head>
<meta charset="utf-8">
<title>Business Search</title>
<link rel="stylesheet" href="https://fonts.googleapis.com/css2?family=Arimo:wght@400;700&display=swap">
<style>
  :root {
    --status-bg: #19232d;
    --status-fg: #ffffff;
    --header-bg: #f5d71e;
    --header-title: #5b4a17;
    --header-fg: #ffffff;
    --list-bg: #ebebec;
    --divider: #b9b9bb;
    --icon-grey: #8f8f91;
    --icon-dark: #555555;
    --heron: #e8436a;
    --willow: #5a5a5c;
    --formwell: #4a4a4c;
    --amber: #f0821e;
    --pulse: #2d4c6e;
    --leaf: #6dbb3a;
    --flower: #d8141c;
  }
  * { box-sizing: border-box; margin: 0; padding: 0; }
  html, body {
    width: 1200px; height: 2298px; overflow: hidden;
    background: var(--list-bg);
    font-family: "Arimo", Arial, sans-serif;
  }
  .screen { width: 1200px; height: 2298px; position: relative; background: var(--list-bg); }

  .status-bar {
    height: 73px; background: var(--status-bg); color: var(--status-fg);
    display: flex; align-items: center; padding: 0 22px; position: relative;
    font-size: 34px; font-weight: 700;
  }
  .status-bar .signal { display: flex; align-items: flex-end; gap: 4px; margin-right: 10px; height: 26px; }
  .status-bar .signal span { width: 6px; background: var(--status-fg); }
  .status-bar .carrier { letter-spacing: 1px; }
  .status-bar .network { margin-left: 18px; }
  .status-bar .lock { position: absolute; left: 575px; top: 18px; }
  .status-bar .battery { position: absolute; right: 22px; top: 22px; }

  .app-header { height: 212px; background: var(--header-bg); position: relative; }
  .app-header .back { position: absolute; left: 56px; top: 78px; }
  .app-header .title {
    position: absolute; left: 128px; top: 30px;
    font-size: 70px; font-weight: 700; color: var(--header-title); letter-spacing: -0.5px;
  }
  .app-header .welcome {
    position: absolute; left: 128px; top: 128px; color: var(--header-fg);
    display: flex; align-items: baseline; gap: 14px;
  }
  .welcome .label { font-size: 38px; font-weight: 700; }
  .welcome .user { font-size: 54px; font-weight: 700; }
  .welcome .network-name { font-size: 38px; font-weight: 700; color: var(--status-bg); margin-left: 8px; }
  .app-header .search { position: absolute; left: 958px; top: 58px; }
  .app-header .menu { position: absolute; left: 1083px; top: 52px; }

  .business-list { list-style: none; padding: 0 56px; }
  .business-row {
    height: 342px; position: relative; border-bottom: 4px solid var(--divider);
    display: flex; align-items: center;
  }
  .business-row .mark { width: 130px; height: 130px; border-radius: 50%; margin-left: 18px; flex: none; }
  .business-row .name {
    margin-left: 32px; font-size: 56px; font-weight: 400; letter-spacing: 0.5px;
    width: 440px; white-space: nowrap;
  }
  .business-row .thumb {
    position: absolute; left: 632px; top: 46px; width: 248px; height: 248px;
    border-radius: 8px; border: 3px solid #d6d6d6;
  }
  .business-row .play { position: absolute; left: 916px; top: 66px; }
  .business-row .delete { position: absolute; left: 1011px; top: 186px; }

  .heron .name { color: var(--heron); }
  .heron .mark { background: #d9d9db; }
  .heron .thumb { background: linear-gradient(160deg, #d8b8a0, #f2e2d6 55%, #ffffff); }
  .willow .name { color: var(--willow); }
  .willow .mark { background: var(--leaf); }
  .willow .thumb { background: linear-gradient(150deg, #e8c4b4, #f6e6df 60%, #ffffff); }
  .formwell .name { color: var(--formwell); }
  .formwell .mark { background: var(--flower); }
  .formwell .thumb { background: linear-gradient(170deg, #d9d6cf, #bfb8ad 55%, #c8201c 85%, #f1efea); }
  .amber .name { color: var(--amber); }
  .amber .mark { background: #f6a316; }
  .amber .thumb { background: linear-gradient(180deg, #cfc8c0, #b58d6c 45%, #2a2826 80%, #e6e4e1); }
  .pulse .name { color: var(--pulse); }
  .pulse .mark { background: transparent; border: 5px solid #b8b8ba; }
  .pulse .thumb { background: linear-gradient(150deg, #f6d3e3, #e44fa0 55%, #f7dce8); }
</style>
</head>
<body>
<main class="screen">
  <header class="status-bar">
    <div class="signal"><span style="height:8px"></span><span style="height:13px"></span><span style="height:18px"></span><span style="height:23px"></span><span style="height:28px"></span></div>
    <span class="carrier">ORBIT</span>
    <span class="network">3G</span>
    <svg class="lock" width="28" height="38" viewBox="0 0 28 38" aria-hidden="true">
      <path d="M7 16V11a7 7 0 0 1 14 0v5" fill="none" stroke="#fff" stroke-width="4"/>
      <rect x="2" y="16" width="24" height="20" rx="2" fill="#fff"/>
    </svg>
    <svg class="battery" width="76" height="30" viewBox="0 0 76 30" aria-hidden="true">
      <rect x="2" y="2" width="66" height="26" rx="4" fill="none" stroke="#fff" stroke-width="3"/>
      <rect x="7" y="7" width="56" height="16" fill="#fff"/>
      <rect x="69" y="10" width="5" height="10" fill="#fff"/>
    </svg>
  </header>

  <section class="app-header">
    <svg class="back" width="36" height="60" viewBox="0 0 36 60" aria-hidden="true">
      <path d="M30 6 L8 30 L30 54" fill="none" stroke="#5b4a17" stroke-width="7" stroke-linecap="round" stroke-linejoin="round"/>
    </svg>
    <h1 class="title">Business Search</h1>
    <p class="welcome">
      <span class="label">Welcome</span>
      <span class="user">Dawson</span>
      <span class="network-name">chatterloop</span>
    </p>
    <svg class="search" width="96" height="96" viewBox="0 0 96 96" aria-label="Search" role="img">
      <circle cx="38" cy="38" r="26" fill="none" stroke="#fff" stroke-width="10"/>
      <path d="M58 58 L86 86" stroke="#fff" stroke-width="13" stroke-linecap="round"/>
    </svg>
    <svg class="menu" width="30" height="108" viewBox="0 0 30 108" aria-label="Menu" role="img">
      <rect x="3" y="4" width="24" height="24" rx="4" fill="#fff"/>
      <rect x="3" y="42" width="24" height="24" rx="4" fill="#fff"/>
      <rect x="3" y="80" width="24" height="24" rx="4" fill="#fff"/>
    </svg>
  </section>

  <ul class="business-list">
    <li class="business-row heron">
      <span class="mark"></span><span class="name">Heron Spa</span>
      <div class="thumb" role="img" aria-label="Photo of a relaxed spa guest"></div>
      <svg class="play" width="84" height="84" viewBox="0 0 84 84" aria-label="Play" role="img"><circle cx="42" cy="42" r="38" fill="none" stroke="#555" stroke-width="5"/><path d="M33 26 L60 42 L33 58 Z" fill="#555"/></svg>
      <svg class="delete" width="56" height="64" viewBox="0 0 56 64" aria-label="Delete" role="img"><rect x="4" y="6" width="48" height="6" fill="#8f8f91"/><rect x="20" y="0" width="16" height="6" fill="#8f8f91"/><path d="M9 16 H47 L44 62 H12 Z" fill="#8f8f91"/><path d="M20 22 V56 M28 22 V56 M36 22 V56" stroke="#ebebec" stroke-width="3"/></svg>
    </li>
    <li class="business-row willow">
      <span class="mark"></span><span class="name">Willow Spa Care</span>
      <div class="thumb" role="img" aria-label="Photo of a foot care treatment"></div>
      <svg class="play" width="84" height="84" viewBox="0 0 84 84" aria-label="Play" role="img"><circle cx="42" cy="42" r="38" fill="none" stroke="#555" stroke-width="5"/><path d="M33 26 L60 42 L33 58 Z" fill="#555"/></svg>
      <svg class="delete" width="56" height="64" viewBox="0 0 56 64" aria-label="Delete" role="img"><rect x="4" y="6" width="48" height="6" fill="#8f8f91"/><rect x="20" y="0" width="16" height="6" fill="#8f8f91"/><path d="M9 16 H47 L44 62 H12 Z" fill="#8f8f91"/><path d="M20 22 V56 M28 22 V56 M36 22 V56" stroke="#ebebec" stroke-width="3"/></svg>
    </li>
    <li class="business-row formwell">
      <span class="mark"></span><span class="name">Formwell</span>
      <div class="thumb" role="img" aria-label="Photo of spa stones with a red flower"></div>
      <svg class="play" width="84" height="84" viewBox="0 0 84 84" aria-label="Play" role="img"><circle cx="42" cy="42" r="38" fill="none" stroke="#555" stroke-width="5"/><path d="M33 26 L60 42 L33 58 Z" fill="#555"/></svg>
      <svg class="delete" width="56" height="64" viewBox="0 0 56 64" aria-label="Delete" role="img"><rect x="4" y="6" width="48" height="6" fill="#8f8f91"/><rect x="20" y="0" width="16" height="6" fill="#8f8f91"/><path d="M9 16 H47 L44 62 H12 Z" fill="#8f8f91"/><path d="M20 22 V56 M28 22 V56 M36 22 V56" stroke="#ebebec" stroke-width="3"/></svg>
    </li>
    <li class="business-row amber">
      <span class="mark"></span><span class="name">Amber Beauty</span>
      <div class="thumb" role="img" aria-label="Photo of a body care treatment"></div>
      <svg class="play" width="84" height="84" viewBox="0 0 84 84" aria-label="Play" role="img"><circle cx="42" cy="42" r="38" fill="none" stroke="#555" stroke-width="5"/><path d="M33 26 L60 42 L33 58 Z" fill="#555"/></svg>
      <svg class="delete" width="56" height="64" viewBox="0 0 56 64" aria-label="Delete" role="img"><rect x="4" y="6" width="48" height="6" fill="#8f8f91"/><rect x="20" y="0" width="16" height="6" fill="#8f8f91"/><path d="M9 16 H47 L44 62 H12 Z" fill="#8f8f91"/><path d="M20 22 V56 M28 22 V56 M36 22 V56" stroke="#ebebec" stroke-width="3"/></svg>
    </li>
    <li class="business-row pulse">
      <span class="mark"></span><span class="name">Pulse Fitness</span>
      <div class="thumb" role="img" aria-label="Photo of manicured pink nails"></div>
      <svg class="play" width="84" height="84" viewBox="0 0 84 84" aria-label="Play" role="img"><circle cx="42" cy="42" r="38" fill="none" stroke="#555" stroke-width="5"/><path d="M33 26 L60 42 L33 58 Z" fill="#555"/></svg>
      <svg class="delete" width="56" height="64" viewBox="0 0 56 64" aria-label="Delete" role="img"><rect x="4" y="6" width="48" height="6" fill="#8f8f91"/><rect x="20" y="0" width="16" height="6" fill="#8f8f91"/><path d="M9 16 H47 L44 62 H12 Z" fill="#8f8f91"/><path d="M20 22 V56 M28 22 V56 M36 22 V56" stroke="#ebebec" stroke-width="3"/></svg>
    </li>
  </ul>
</main>
</body>
</html>
```